educational services
broker of essential services
So I love my Velvet Kettle cards. I love the background.
I like the background on the coral ridge card
I like a little part of each Monarch card
I want my card to stand out and be professional
I would also like somewhat of a brand
I do not want it to be specific to anything but the world and galaxy
I would like to be able to be used for everything, all encompassing
In spanish Sin paredes, not sureother languages but i will do programs for other countries like China, Japan and Korea
Reason: It has been the first week of school and I have not been able to get the feedback I need.
Please change colors to Blue and GOld
Please add ~ over the n in Lorna
Please submit some vertical designs
Please include the world
Please make eagle a watermark
Make sure the Open Horizon doesnt have "preparatory school" under it
I am open to new designs and I will pay more after I chose a designer who seems to get all this stuff in my head!
Reason: Last minute designs were wonderful
Reason: I was out of town and not able to review the wonderful designs posted. I am narrowing the designs down now! I appreciate all the work done thus far.
Hello,
Thank you for all the designs. This is difficult. I have not been able to access them as I was able to last week so please be patient. If you also do web design please send me a message.
Again, thank you. I am down to just a few designs.
Sincerely,
Lorna Vidal Pratchett
I have been extremely busy, I should pick a design by the ned of this week. Thank you for your patience
Business
Dr. Lorna Vidal Pratchett
www.ohacademy-example.com
(555) 284-9071 US
lornajanevidal@mailbox-example.com

```html
<!DOCTYPE html>
<html lang="en">
<head>
<meta charset="utf-8">
<title>Open Horizon – Business Card</title>
<link rel="stylesheet" href="https://fonts.googleapis.com/css2?family=Libre+Baskerville:wght@400;700&family=Questrial&family=Great+Vibes&display=swap">
<style>
  :root{
    --stage:#ece8e3;
    --magenta:#8e1455;
    --magenta-deep:#5c0936;
    --magenta-soft:#b02a73;
    --gold:#d9cf45;
    --gold-text:#e6dc6a;
    --paper:#ffffff;
    --eagle-light:#e4e4e4;
    --eagle-mid:#a8a8a8;
  }
  *{margin:0;padding:0;box-sizing:border-box}
  html,body{width:1200px;height:1023px;overflow:hidden;background:var(--stage)}
  .stage{position:relative;width:1200px;height:1023px}
  .card{position:absolute;left:250px;width:700px;height:400px;overflow:hidden;border-radius:4px;
        box-shadow:0 6px 18px rgba(0,0,0,.18)}
  .card--front{top:85px}
  .card--back{top:535px;background:linear-gradient(135deg,var(--magenta-deep) 0%,var(--magenta) 45%,var(--magenta-soft) 100%)}
  .card svg.art{position:absolute;inset:0}

  .holder-name{position:absolute;left:40px;top:28px;font-family:"Libre Baskerville",serif;font-weight:700;
               font-size:30px;color:var(--gold-text);letter-spacing:.3px;white-space:nowrap}
  .contact{position:absolute;left:62px;top:92px;list-style:none;font-family:"Libre Baskerville",serif;
           font-size:15px;color:var(--gold-text);line-height:24px}
  .contact li{display:flex;align-items:center;gap:9px;white-space:nowrap}
  .contact svg{width:13px;height:13px;flex:none}

  .brand{position:absolute;left:40px;top:312px;display:flex;align-items:center;gap:10px;height:40px}
  .brand-dot{width:34px;height:34px;border-radius:50%;background:var(--magenta);flex:none}
  .brand-name{font-family:"Questrial",sans-serif;font-size:38px;line-height:40px;color:var(--gold);
              letter-spacing:1px;white-space:nowrap}

  .tagline{position:absolute;right:40px;top:170px;font-family:"Great Vibes",cursive;font-size:34px;
           color:var(--gold-text);white-space:nowrap}
</style>
</head>
<body>
<main class="stage">

  <section class="card card--front">
    <svg class="art" viewBox="0 0 700 400" width="700" height="400">
      <defs>
        <linearGradient id="front-bg" x1="0" y1="0" x2="1" y2="1">
          <stop offset="0" stop-color="#a3266a"/>
          <stop offset="1" stop-color="#7a0f48"/>
        </linearGradient>
        <radialGradient id="eagle-fill" cx=".5" cy=".5" r=".5">
          <stop offset="0" stop-color="var(--eagle-mid)"/>
          <stop offset="1" stop-color="var(--eagle-light)" stop-opacity="0"/>
        </radialGradient>
      </defs>
      <rect class="base" width="700" height="400" fill="url(#front-bg)"/>
      <path class="swoosh-gold" d="M0,290 C150,190 340,200 470,118 C570,60 640,22 700,20 L700,60 C640,60 580,95 480,150 C350,222 150,225 0,318 Z" fill="var(--gold)"/>
      <path class="swoosh-paper" d="M0,314 C150,222 350,222 480,150 C580,95 640,62 700,60 L700,400 L0,400 Z" fill="var(--paper)"/>
      <line class="name-rule" x1="40" y1="76" x2="560" y2="76" stroke="var(--gold)" stroke-width="1"/>
      <rect class="brand-bar" x="410" y="321" width="270" height="22" rx="11" fill="var(--magenta)"/>
      <ellipse role="img" aria-label="Soaring eagle illustration" cx="330" cy="262" rx="120" ry="26" fill="url(#eagle-fill)"/>
    </svg>

    <h1 class="holder-name">Dr. Lorna Vidal Pratchett</h1>
    <ul class="contact">
      <li><svg viewBox="0 0 12 12"><rect width="12" height="12" rx="2" fill="var(--gold)"/><path d="M3.5 2.5l1.4 1.6-.8 1a5 5 0 0 0 1.8 1.8l1-.8 1.6 1.4-.9 1.2C5.5 8.7 3.3 6.5 2.4 3.4z" fill="var(--magenta)"/></svg>(555) 284-9071 US</li>
      <li><svg viewBox="0 0 12 12"><rect width="12" height="12" rx="2" fill="var(--gold)"/><path d="M2.5 3.5h7v5h-7z M2.5 3.5l3.5 3 3.5-3" fill="none" stroke="var(--magenta)" stroke-width="1"/></svg>lornajanevidal@mailbox-example.com</li>
      <li><svg viewBox="0 0 12 12"><rect width="12" height="12" rx="2" fill="var(--gold)"/><circle cx="6" cy="6" r="3.5" fill="none" stroke="var(--magenta)" stroke-width="1"/><path d="M2.5 6h7M6 2.5v7" stroke="var(--magenta)" stroke-width=".8"/></svg>www.ohacademy-example.com</li>
    </ul>

    <div class="brand">
      <span class="brand-dot"></span>
      <span class="brand-name">OPEN HORIZON</span>
    </div>
  </section>

  <section class="card card--back">
    <svg class="art" viewBox="0 0 700 400" width="700" height="400">
      <defs>
        <radialGradient id="watermark-fill" cx=".5" cy=".5" r=".5">
          <stop offset="0" stop-color="var(--magenta-deep)" stop-opacity=".55"/>
          <stop offset="1" stop-color="var(--magenta-deep)" stop-opacity="0"/>
        </radialGradient>
      </defs>
      <ellipse role="img" aria-label="Faint eagle watermark" cx="190" cy="170" rx="190" ry="130" fill="url(#watermark-fill)"/>
      <ellipse role="img" aria-label="Faint world map watermark" cx="500" cy="270" rx="180" ry="90" fill="url(#watermark-fill)"/>
    </svg>
    <p class="tagline">Where the horizon stays open to your success</p>
  </section>

</main>
</body>
</html>
```